Vorandel

Legal Website that specializes in traffic ticket defense and DUIs. We would like regular business cards, however, we would like cards that look like a parking ticket that is usually in an envelope and placed on front window of a parked car. The prices are 99 for speeding ticket and 49 for non-moving violations. No points or your money back. www.vorandel-example.com is our old website.
Updates

I like a lot of these designs and some of them would really be great for a personal business card. However, I would really like to see some cards that look like a parking or speeding ticket. We also want to see the marketing on the ticket. No point guarantee, $99 etc.

Industry/Entity Type

Defense

```html
<!DOCTYPE html>
<html lang="en">
<head>
<meta charset="utf-8">
<title>Vorandel – Traffic Ticket Defense Card</title>
<link rel="stylesheet" href="https://fonts.googleapis.com/css2?family=Oswald:wght@400;500;700&family=Roboto+Condensed:wght@400;700&display=swap">
<style>
  :root {
    --page-bg: #d6d6d6;
    --card-edge: #1e1e1e;
    --ticket-orange: #f3a72a;
    --ticket-line: #3b2c12;
    --badge-dark: #2f3236;
    --badge-text: #f3f3f3;
    --accent-green: #5a9b2c;
    --accent-yellow: #f7c531;
    --accent-red: #c8321f;
    --ink-white: #ffffff;
  }
  * { box-sizing: border-box; margin: 0; padding: 0; }
  html, body { width: 1200px; height: 927px; overflow: hidden; }
  body {
    background: var(--page-bg);
    font-family: "Roboto Condensed", "Arial Narrow", sans-serif;
    position: relative;
  }
  .ticket-card {
    position: absolute;
    left: 150px; top: 203px;
    width: 900px; height: 520px;
  }
  .ticket-shape { position: absolute; inset: 0; }
  .badge-row {
    position: absolute;
    top: 78px; left: 0; right: 0;
    display: flex; justify-content: center; gap: 26px;
  }
  .badge {
    width: 210px; height: 78px;
    background: var(--badge-dark);
    display: flex; align-items: center; gap: 12px;
    padding: 0 14px;
    color: var(--badge-text);
  }
  .badge svg { flex: none; }
  .badge-text { font-family: "Oswald", sans-serif; line-height: 1.15; }
  .badge-small { font-size: 13px; font-weight: 400; letter-spacing: 0.5px; }
  .badge-big { font-size: 22px; font-weight: 700; color: var(--accent-yellow); letter-spacing: 0.5px; }
  .badge-big.green { color: #8cc63f; font-size: 20px; }
  .headline {
    position: absolute;
    top: 180px; left: 0; right: 0;
    text-align: center;
    font-family: "Oswald", sans-serif;
    font-weight: 700; font-size: 40px;
    color: var(--ink-white);
    letter-spacing: 0.5px;
  }
  .headline .lead { color: var(--accent-green); }
  .call-block {
    position: absolute;
    top: 262px; left: 100px;
    width: 260px; text-align: center;
  }
  .call-label {
    font-family: "Oswald", sans-serif;
    font-size: 17px; color: var(--ink-white);
    margin-top: 2px; letter-spacing: 1px;
  }
  .call-number {
    font-family: "Oswald", sans-serif;
    font-size: 30px; color: var(--accent-red);
    line-height: 1.2;
  }
  .firm-name {
    font-family: "Oswald", sans-serif;
    font-size: 22px; font-weight: 700; color: var(--badge-dark);
    letter-spacing: 3px; margin-top: 8px;
  }
  .firm-web {
    font-family: "Oswald", sans-serif;
    font-size: 14px; color: var(--badge-dark);
  }
  .promise-list {
    position: absolute;
    top: 276px; left: 420px;
    list-style: none;
    font-family: "Oswald", sans-serif;
    font-size: 18px; color: var(--ink-white);
  }
  .promise-list li {
    display: flex; align-items: center; gap: 12px;
    margin-bottom: 18px;
  }
  .promise-list .detail { color: var(--ticket-line); font-size: 16px; margin-left: 6px; }
  .promise-list .price { color: var(--accent-red); font-weight: 700; }
</style>
</head>
<body>
  <main class="ticket-card">
    <svg class="ticket-shape" viewBox="0 0 900 520" width="900" height="520" aria-hidden="true">
      <defs>
        <pattern id="perf-h" width="30" height="20" patternUnits="userSpaceOnUse" x="0" y="-10">
          <circle cx="15" cy="10" r="9" fill="black"/>
        </pattern>
        <pattern id="perf-v" width="20" height="30" patternUnits="userSpaceOnUse" x="-10" y="0">
          <circle cx="10" cy="15" r="9" fill="black"/>
        </pattern>
        <mask id="perforation">
          <rect width="900" height="520" fill="white"/>
          <rect x="0" y="-10" width="900" height="20" fill="url(#perf-h)"/>
          <rect x="0" y="510" width="900" height="20" fill="url(#perf-h)"/>
          <rect x="-10" y="0" width="20" height="520" fill="url(#perf-v)"/>
          <rect x="890" y="0" width="20" height="520" fill="url(#perf-v)"/>
        </mask>
      </defs>
      <rect width="900" height="520" fill="var(--card-edge)" mask="url(#perforation)"/>
      <rect x="30" y="30" width="840" height="460" fill="var(--ticket-orange)"/>
      <rect x="62" y="58" width="776" height="404" rx="26" fill="none" stroke="var(--ticket-line)" stroke-width="2"/>
      <line class="tear-line" x1="390" y1="262" x2="390" y2="440" stroke="var(--ticket-line)" stroke-width="2" stroke-dasharray="6 5"/>
    </svg>

    <section class="badge-row">
      <div class="badge">
        <svg width="40" height="40" viewBox="0 0 40 40" aria-hidden="true">
          <rect x="7" y="7" width="26" height="26" transform="rotate(45 20 20)" fill="var(--accent-yellow)"/>
          <path d="M15 25 L20 14 L25 25 Z" fill="var(--badge-dark)"/>
        </svg>
        <div class="badge-text">
          <div class="badge-small">OVER 1 MILLION</div>
          <div class="badge-small">TICKETS DEFENDED</div>
        </div>
      </div>
      <div class="badge">
        <svg width="40" height="40" viewBox="0 0 40 40" aria-hidden="true">
          <circle cx="20" cy="20" r="15" fill="none" stroke="#ffffff" stroke-width="8"/>
          <circle cx="20" cy="20" r="15" fill="none" stroke="#e0522a" stroke-width="8" stroke-dasharray="11.8 11.8"/>
        </svg>
        <div class="badge-text">
          <div class="badge-small">LOWEST PRICE</div>
          <div class="badge-big green">GUARANTEE</div>
        </div>
      </div>
      <div class="badge">
        <svg width="40" height="40" viewBox="0 0 40 40" aria-hidden="true">
          <path d="M20 5 L37 35 L3 35 Z" fill="var(--accent-yellow)"/>
          <rect x="18.5" y="15" width="3" height="11" fill="var(--badge-dark)"/>
          <rect x="18.5" y="28" width="3" height="3" fill="var(--badge-dark)"/>
        </svg>
        <div class="badge-text">
          <div class="badge-big">24-HOUR</div>
          <div class="badge-small">TICKET HOTLINE</div>
        </div>
      </div>
    </section>

    <h1 class="headline"><span class="lead">START YOUR</span> TRAFFIC TICKET DEFENSE!</h1>

    <section class="call-block">
      <svg width="42" height="42" viewBox="0 0 46 46" aria-hidden="true">
        <path d="M12 6 C9 6 6 10 7 15 C9 26 20 37 31 39 C36 40 40 37 40 34 L40 30 L32 26 L28 30 C22 27 19 24 16 18 L20 14 L16 6 Z" fill="var(--badge-dark)"/>
        <path d="M28 10 A10 10 0 0 1 36 18" fill="none" stroke="var(--badge-dark)" stroke-width="2.5"/>
        <path d="M28 4 A16 16 0 0 1 42 18" fill="none" stroke="var(--badge-dark)" stroke-width="2.5"/>
      </svg>
      <div class="call-label">CALL NOW :</div>
      <div class="call-number">(555) 014 2020</div>
      <div class="firm-name">VORANDEL</div>
      <div class="firm-web">www.vorandel-example.com</div>
    </section>

    <ul class="promise-list">
      <li>
        <svg width="22" height="22" viewBox="0 0 22 22" aria-hidden="true"><path d="M3 12 L9 18 L20 4" fill="none" stroke="var(--accent-green)" stroke-width="3.5"/></svg>
        <span>LOWEST PRICE GUARANTEE!<span class="detail">Call for Details!</span></span>
      </li>
      <li>
        <svg width="22" height="22" viewBox="0 0 22 22" aria-hidden="true"><path d="M3 12 L9 18 L20 4" fill="none" stroke="var(--accent-green)" stroke-width="3.5"/></svg>
        <span>OVER 1 MILLION TICKETS RESOLVED!</span>
      </li>
      <li>
        <svg width="22" height="22" viewBox="0 0 22 22" aria-hidden="true"><path d="M3 12 L9 18 L20 4" fill="none" stroke="var(--accent-green)" stroke-width="3.5"/></svg>
        <span>NO POINTS OR YOUR MONEY BACK!</span>
      </li>
      <li>
        <svg width="22" height="22" viewBox="0 0 22 22" aria-hidden="true"><path d="M3 12 L9 18 L20 4" fill="none" stroke="var(--accent-green)" stroke-width="3.5"/></svg>
        <span><span class="price">$99</span> SPEEDING &nbsp;·&nbsp; <span class="price">$49</span> NON-MOVING</span>
      </li>
    </ul>
  </main>
</body>
</html>
```